Naturopath specialising in Children's Health

I have just started working in a new clinic where I will be predominantly treating children so I would like to rebrand with a business card that reflects this.

I would like a clever design which is subtly playful and will attract children and parents alike, while maintaining a professional look. It must also reflect that I utilize natural medicine - including herbal medicine and nutrition as part of my treatment. Employing the use of a plant or herb would be ideal. I had envisioned the image of a dandelion blowing in the wind (or being blown by a child) as a great combination of the playful yet natural medicine I am trying to ecompass in the card.

I would like to use yellow, orange, blue or green as the dominant colour for the card.

The front of the card should contain the logo and the words 'Maribel Stroud - Naturopath.'

The back of the card should contain the following details:
Maribel Stroud BHSc Nat, Dip RM
Naturopath, Herbalist, Nutritionist, Iridologist, Remedial Massage Therapist, Reiki Practitioner
0413 927 186
Willowfern Haven - (02) 9731 4068
maribel.stroud@kestrelmail.example
NHPA 81347

Industry/Entity Type

Clinic

```html
<!DOCTYPE html>
<html lang="en">
<head>
<meta charset="utf-8">
<title>Maribel Stroud Naturopath – Business Cards</title>
<link rel="stylesheet" href="https://fonts.googleapis.com/css2?family=Exo+2:wght@700;800&family=Open+Sans:wght@400;600&display=swap">
<style>
  :root {
    --backdrop: #e9e9ea;
    --card: #ffffff;
    --ink: #1d1d1f;
    --muted: #55555a;
    --accent-green: #3f9b3a;
    --accent-orange: #f39a1e;
    --corner-green: #1f5e3a;
    --mark-dot: #f6b51b;
    --seed-light: #fbf3c8;
    --seed-mid: #e9d87a;
  }
  * { box-sizing: border-box; margin: 0; padding: 0; }
  html, body {
    width: 1200px;
    height: 735px;
    overflow: hidden;
    background: var(--backdrop);
  }
  .stage {
    position: relative;
    width: 1200px;
    height: 735px;
  }
  .card {
    position: absolute;
    top: 212px;
    width: 540px;
    height: 310px;
    background: var(--card);
    box-shadow: 0 6px 18px rgba(0,0,0,0.12);
    overflow: hidden;
  }
  .card--front { left: 40px; }
  .card--back { left: 620px; }
  .card__swoosh {
    position: absolute;
    inset: 0;
    width: 540px;
    height: 310px;
  }

  /* Front */
  .brand-mark {
    position: absolute;
    left: 70px;
    top: 70px;
    display: flex;
    align-items: center;
    gap: 12px;
    font-family: "Open Sans", sans-serif;
    font-weight: 600;
    font-size: 22px;
    color: var(--ink);
  }
  .brand-mark__dot {
    width: 44px;
    height: 44px;
    border-radius: 50%;
    background: var(--mark-dot);
    flex: none;
  }
  .holder {
    position: absolute;
    left: 70px;
    top: 150px;
  }
  .holder__name {
    font-family: "Open Sans", sans-serif;
    font-weight: 600;
    font-size: 19px;
    letter-spacing: 0.3px;
    color: var(--ink);
    text-transform: uppercase;
  }
  .holder__role {
    font-family: "Open Sans", sans-serif;
    font-weight: 400;
    font-size: 16px;
    color: var(--accent-green);
    margin-top: 2px;
  }
  .dandelion {
    position: absolute;
    left: 360px;
    top: 150px;
    width: 120px;
    height: 120px;
    border-radius: 50%;
    background: radial-gradient(circle, var(--seed-light) 0%, var(--seed-mid) 70%, rgba(233,216,122,0) 100%);
  }

  /* Back */
  .back-dot {
    position: absolute;
    left: 38px;
    top: 62px;
    width: 30px;
    height: 30px;
    border-radius: 50%;
    background: var(--mark-dot);
  }
  .practitioner {
    position: absolute;
    left: 82px;
    top: 56px;
    font-family: "Exo 2", sans-serif;
    font-weight: 800;
    font-size: 28px;
    line-height: 1.05;
    letter-spacing: 0.5px;
    color: var(--ink);
    text-transform: uppercase;
  }
  .credentials {
    position: absolute;
    left: 38px;
    top: 124px;
    width: 330px;
    font-family: "Open Sans", sans-serif;
    color: var(--muted);
  }
  .credentials__quals {
    font-size: 12px;
    font-weight: 600;
    color: var(--accent-green);
  }
  .credentials__titles {
    font-size: 11px;
    line-height: 1.35;
    margin-top: 2px;
  }
  .contact-list {
    position: absolute;
    left: 38px;
    top: 186px;
    list-style: none;
    font-family: "Open Sans", sans-serif;
    font-size: 11px;
    color: var(--muted);
  }
  .contact-list li {
    display: flex;
    align-items: center;
    gap: 8px;
    height: 19px;
  }
  .contact-list svg {
    width: 11px;
    height: 11px;
    fill: var(--accent-green);
    flex: none;
  }
</style>
</head>
<body>
<main class="stage">

  <section class="card card--front">
    <svg class="card__swoosh" viewBox="0 0 540 310" aria-hidden="true">
      <path d="M330 0 H540 V72 C480 32 410 8 330 0 Z" fill="var(--corner-green)"/>
      <path d="M150 0 C330 6 470 42 540 92 L540 80 C465 32 330 4 210 0 Z" fill="var(--accent-orange)"/>
    </svg>
    <div class="brand-mark">
      <span class="brand-mark__dot"></span>
      <span>Maribel Stroud</span>
    </div>
    <div class="holder">
      <p class="holder__name">Maribel Stroud</p>
      <p class="holder__role">Naturopath</p>
    </div>
    <div class="dandelion" role="img" aria-label="Dandelion seed head blowing in the wind"></div>
  </section>

  <section class="card card--back">
    <svg class="card__swoosh" viewBox="0 0 540 310" aria-hidden="true">
      <path d="M330 0 H540 V72 C480 32 410 8 330 0 Z" fill="var(--corner-green)"/>
      <path d="M150 0 C330 6 470 42 540 92 L540 80 C465 32 330 4 210 0 Z" fill="var(--accent-orange)"/>
      <path d="M540 310 H320 C410 302 485 282 540 246 Z" fill="var(--corner-green)"/>
      <path d="M130 310 C330 306 470 282 540 228 L540 240 C470 292 330 310 190 310 Z" fill="var(--accent-orange)"/>
    </svg>
    <span class="back-dot"></span>
    <h1 class="practitioner">Maribel Stroud<br>Naturopath</h1>
    <div class="credentials">
      <p class="credentials__quals">BHSc Nat, Dip RM</p>
      <p class="credentials__titles">Naturopath, Herbalist, Nutritionist, Iridologist, Remedial Massage Therapist, Reiki Practitioner</p>
    </div>
    <ul class="contact-list">
      <li>
        <svg viewBox="0 0 12 12"><path d="M3 0h6a1 1 0 0 1 1 1v10a1 1 0 0 1-1 1H3a1 1 0 0 1-1-1V1a1 1 0 0 1 1-1zm0 1.5v8h6v-8z"/></svg>
        0413 927 186
      </li>
      <li>
        <svg viewBox="0 0 12 12"><path d="M2.5 0.5 L4.5 0.5 L5.3 3.2 L3.9 4.4 C4.6 6 6 7.4 7.6 8.1 L8.8 6.7 L11.5 7.5 L11.5 9.5 C11.5 10.6 10.6 11.5 9.5 11.5 C4.5 11.2 0.8 7.5 0.5 2.5 C0.5 1.4 1.4 0.5 2.5 0.5 Z"/></svg>
        Willowfern Haven - (02) 9731 4068
      </li>
      <li>
        <svg viewBox="0 0 12 12"><path d="M1 2h10a1 1 0 0 1 1 1v6a1 1 0 0 1-1 1H1a1 1 0 0 1-1-1V3a1 1 0 0 1 1-1zm0 1.3V9h10V3.3L6 6.6z"/></svg>
        maribel.stroud@kestrelmail.example
      </li>
      <li>
        <svg viewBox="0 0 12 12"><path d="M2 5.5 L4.8 8.5 L10 2.8 L11.2 4 L4.8 11 L0.8 6.7 Z"/></svg>
        NHPA 81347
      </li>
    </ul>
  </section>

</main>
</body>
</html>
```